Marlow Yardcraft need a flyer - A6 - Double sided

We need a flyer that will engage potential customer in need for gardening services. We offer high quality gardening services spanning from lawn mowing and weeding to soil improvement to tree pruning and so on.
I would like a double sided flyer A6 size. I trust your expert touch in terms of lay out but the general idea I had was to have one side with the logo, a catchy picture (or more), the website/phone number/address and on the flip side a little more text focusing on the client perspective with statement such as 'Let us do the hard work so that you can enjoy your garden' (obviously the wording isn't my strongest skill) but the idea is to get into the customer perspective;
I would also like to list all the service we can offer such as but not limited to weeding, pruning, lawn care, green waste disposal, soil improvement, hedging, edging, lawn mowing,...
Happy for you to use any picture free of right from the internet if necessary

Target Market(s)

Home owner & Businesses

Industry/Entity Type

Landscape Gardening

Requirements
Must have
• website - http://yardcraft-marlow.com.au (feel free to browse the website to get ideas on color theme and overall look)
• phone number - (08) 6341 2705
Nice to have
• a list of services on offer
• phone number and website
• being customer perspective focused (the benefits for the customer) - perhaps on the flip side some text like 'highly trained and experienced landscape gardeners so that the job is done perfectly every time', 'always carrying all range of commercial grade tools so that we can tackle any job', 'Experienced gardeners so that the job is achieve faster' (it doesn't have to be in those exact words as I trust that you may be expert in wording as well as designers?)

```html
<!DOCTYPE html>
<html lang="en">
<head>
<meta charset="utf-8">
<title>Marlow Yardcraft – Flyer Back</title>
<link rel="stylesheet" href="https://fonts.googleapis.com/css2?family=Oswald:wght@500;700&family=Kalam:wght@400&family=Open+Sans:wght@400;600&display=swap">
<style>
  :root {
    --green: #7cb82f;
    --green-dark: #3f6d1c;
    --ink: #2a2a2a;
    --muted: #555555;
    --paper: #ffffff;
    --icon: #1f1f1f;
  }
  * { margin: 0; padding: 0; box-sizing: border-box; }
  html, body { width: 824px; height: 1200px; overflow: hidden; background: var(--paper); }
  .flyer { position: relative; width: 824px; height: 1200px; background: var(--paper); font-family: "Open Sans", sans-serif; color: var(--ink); }
  .side-label { height: 33px; text-align: center; font: 600 14px/33px "Open Sans", sans-serif; letter-spacing: 2px; color: var(--muted); }
  .hero { position: absolute; top: 33px; left: 0; width: 824px; height: 311px;
    background: linear-gradient(160deg, #8fb85a 0%, #4d7a2a 45%, #2f4f1c 80%, #c9d86a 100%); }
  .brand { position: absolute; top: 268px; left: 50%; transform: translateX(-50%); background: var(--paper);
    padding: 16px 36px; font: 700 50px/1 "Oswald", sans-serif; color: var(--green-dark); text-transform: uppercase; letter-spacing: 1px; white-space: nowrap; }
  .headline { position: absolute; top: 372px; left: 0; right: 0; text-align: center; white-space: nowrap;
    font: 700 29px/1.1 "Oswald", sans-serif; color: var(--green); text-transform: uppercase; }
  .intro { position: absolute; top: 414px; left: 52px; right: 52px; text-align: center;
    font: 400 17px/23px "Kalam", cursive; color: var(--ink); }
  .services { position: absolute; top: 560px; left: 27px; width: 770px; display: grid;
    grid-template-columns: repeat(3, 1fr); column-gap: 20px; row-gap: 20px; }
  .service { text-align: center; }
  .service-icon { display: block; margin: 0 auto 6px; width: 52px; height: 52px; border-radius: 7px; background: var(--icon); }
  .service-title { font: 700 15px/1.2 "Oswald", sans-serif; color: var(--green); text-transform: uppercase; margin-bottom: 3px; white-space: nowrap; }
  .service-text { font: 400 12px/16px "Open Sans", sans-serif; color: var(--muted); }
  .website { position: absolute; bottom: 28px; left: 0; right: 0; text-align: center;
    font: 500 36px/1 "Oswald", sans-serif; color: var(--green); }
</style>
</head>
<body>
<div class="flyer">
  <div class="side-label">BACK</div>
  <div class="hero" role="img" aria-label="Smiling gardener in a hi-vis shirt among leafy trees with red flowers"></div>
  <div class="brand">Marlow Yardcraft</div>

  <h1 class="headline">Let us do the hard work so that you can enjoy your garden</h1>

  <p class="intro">Thanks to our years of experience in landscaping, we have the skills and knowledge required to deliver a consistently high quality service. We're here to work with you both now, and in the long-term to help you achieve your garden paradise. Whether you need simple weeding, pruning and garden maintenance or help transforming a backyard jungle, you can trust us – your friendly local gardeners.</p>

  <div class="services">
    <div class="service">
      <span class="service-icon" role="img" aria-label="Lawn mower icon"></span>
      <h2 class="service-title">Lawn Care</h2>
      <p class="service-text">We offer a range of lawn care services including lawn mowing, fertilising, dethatching, aeration and top dressing.</p>
    </div>
    <div class="service">
      <span class="service-icon" role="img" aria-label="Gardener pruning a tree icon"></span>
      <h2 class="service-title">Tree Pruning &amp; Plant Care</h2>
      <p class="service-text">Pruning correctly, and at the right time of year, can transform overgrown, misshapen plants into well-shaped, healthy-growing greenery.</p>
    </div>
    <div class="service">
      <span class="service-icon" role="img" aria-label="Hedge trimmer icon"></span>
      <h2 class="service-title">Hedge Trimming</h2>
      <p class="service-text">Patchy growth can look very untidy – and that's why it's important to get the professionals in to help!</p>
    </div>
    <div class="service">
      <span class="service-icon" role="img" aria-label="Leaf and sprout icon"></span>
      <h2 class="service-title">Organic Gardening</h2>
      <p class="service-text">Offering eco-friendly gardening options for those who wish to avoid the use of chemicals. Organic weed killers, plant treatments and fertilisers.</p>
    </div>
    <div class="service">
      <span class="service-icon" role="img" aria-label="Wheelbarrow of mulch icon"></span>
      <h2 class="service-title">Mulching</h2>
      <p class="service-text">With the right mulch selected and applied, you'll notice the difference it makes both to the appearance of your garden, and the growth.</p>
    </div>
    <div class="service">
      <span class="service-icon" role="img" aria-label="Weeds in soil icon"></span>
      <h2 class="service-title">Weed Control</h2>
      <p class="service-text">Our Marlow garden services provide you with a regular weeding service, combined with weed control methods to keep your garden looking tidy.</p>
    </div>
    <div class="service">
      <span class="service-icon" role="img" aria-label="Green waste bin icon"></span>
      <h2 class="service-title">Rubbish &amp; Green Waste Removal</h2>
      <p class="service-text">Keep your garden clear with fast, affordable rubbish and green waste removal. Just give us a call and our team can come to you to provide a pick-up and disposal service.</p>
    </div>
    <div class="service">
      <span class="service-icon" role="img" aria-label="Hands planting a seedling icon"></span>
      <h2 class="service-title">Fertilising &amp; Soil Improvement</h2>
      <p class="service-text">Soil testing, fertiliser selection and soil care can truly transform your garden. Talk to us about your desired outcome, and our garden services team finds a way to provide the solution.</p>
    </div>
  </div>

  <div class="website">www.yardcraft-marlow.com.au</div>
</div>
</body>
</html>
```